Web Design Project - Maple & Meadow

Live long and prosper!
The page aims people willing to book holidays and health prevention courses in combination. The ZOR-Method is a concept of defined:
* EXERCISES: walking, fitness, yoga, ...
* RELAXATION: massage, spa, ...
* NUTRITION: diets (more, less, selected)
Doing in a group brings fun and social community.
When wanted a doctor or health professional supports the stay.
The page explains all courses, all benefits and all locations to stay.

```html
<!DOCTYPE html>
<html lang="en">
<head>
<meta charset="utf-8">
<title>Maple &amp; Meadow</title>
<link href="https://fonts.googleapis.com/css2?family=Arimo:wght@400;700&family=Cinzel:wght@400;600&family=Tinos:wght@700&family=Ubuntu:wght@400;500;700&display=swap" rel="stylesheet">
<style>
:root{
  --stage:#ffffff;
  --frame:#d6d6d6;
  --white:#ffffff;
  --soft:#f4f4f4;
  --line:#d0d0d0;
  --green:#8cc63e;
  --green-dark:#6fa52a;
  --ink:#222222;
  --text:#555555;
  --muted:#888888;
  --link:#2a9fd6;
}
*{margin:0;padding:0;box-sizing:border-box}
html,body{width:1200px;height:900px;overflow:hidden;background:var(--stage)}
.stage{width:1152px;height:864px;position:relative;transform:scale(1.0417);transform-origin:0 0}
.page{position:absolute;left:333px;top:14px;width:485px;height:829px;background:var(--frame);font-family:"Arimo",sans-serif;color:var(--text)}
.abs{position:absolute}
.logo{left:28px;top:17px;font-family:"Ubuntu",sans-serif;font-weight:700;font-size:14px;color:var(--green);letter-spacing:.2px}
.nav{left:18px;top:38px;width:457px;height:29px;background:var(--white);border:1px solid #e6e6e6;display:flex;align-items:center;padding-left:10px;gap:0}
.nav a{font-family:"Tinos",serif;font-weight:700;font-size:7px;color:#333;text-decoration:none;padding:4px 6px;margin-right:1px}
.nav a.active{background:var(--green);color:#fff;border:2px solid #cfe8a8;padding:3px 6px}
.hero{left:31px;top:81px;width:431px;height:164px;background:linear-gradient(100deg,#6b5a3a 0%,#e8d3a4 18%,#b46a22 32%,#7a3e16 45%,#c9b9a0 58%,#eeeee6 72%,#f8f8f4 85%,#5d6a52 100%)}
.dots{left:233px;top:252px;display:flex;gap:2px}
.dots span{width:5px;height:5px;border-radius:50%;background:#9a9a9a}
.dots span:first-child{background:#666}
.intro{left:18px;top:268px;width:457px;height:108px;background:var(--white)}
.intro h1{position:absolute;left:13px;top:15px;font-family:"Ubuntu",sans-serif;font-weight:500;font-size:11px;color:var(--ink)}
.intro p{position:absolute;left:14px;top:37px;width:150px;font-size:6.6px;line-height:9px}
.btn{display:inline-block;border:1px solid #d6d6d6;background:linear-gradient(#fafafa,#e9e9e9);font-size:7.5px;color:#555;padding:4px 6px;box-shadow:0 1px 1px rgba(0,0,0,.08)}
.intro .btn{position:absolute;left:52px;top:80px}
.intro .divider{position:absolute;left:196px;top:12px;width:1px;height:75px;background:var(--line)}
.thumb{position:absolute;top:14px;width:70px;text-align:center}
.thumb .ph{width:70px;height:70px;border:1px solid #e0e0e0;padding:3px;background:#fff;box-shadow:0 1px 2px rgba(0,0,0,.1)}
.thumb .ph div{width:100%;height:100%}
.thumb span{display:block;margin-top:5px;font-size:6.5px;color:#333}
.mid{left:18px;top:377px;width:457px;height:202px;background:linear-gradient(#ffffff,#f3f3f3);border-top:1px solid #dcdcdc}
h2{font-family:"Cinzel",serif;font-weight:600;font-size:10.5px;color:var(--ink);position:absolute}
.special{position:absolute;left:13px;width:134px;height:40px;border-bottom:1px dashed #bbb}
.special .ph{position:absolute;left:0;top:2px;width:34px;height:34px;background:linear-gradient(135deg,#f0a020,#d84a10 60%,#5a2a10)}
.special b{position:absolute;left:38px;top:0;font-size:6.4px;color:var(--ink)}
.special p{position:absolute;left:38px;top:10px;width:96px;font-size:4.5px;line-height:7px}
.special a{position:absolute;left:38px;top:25px;font-size:4.6px;color:#333;text-decoration:underline}
.hours{position:absolute;left:162px;top:44px;width:125px;font-size:6.2px;line-height:8px}
.hours dt{font-weight:700;color:var(--ink);margin-top:6px}
.hours dt:first-child{margin-top:0}
.map{position:absolute;left:166px;top:108px;width:117px;height:58px;border:1px solid #ddd;background:linear-gradient(120deg,#b9dca6,#e4efd6 50%,#a8cf96)}
.about p{position:absolute;left:306px;width:146px;font-size:6.3px;line-height:8.6px}
.about .btn{position:absolute;left:310px;top:155px}
.lower{left:18px;top:580px;width:457px;height:210px;background:var(--white);border-top:1px solid #e0e0e0}
.tweet{position:absolute;left:19px;width:142px;background:#ececec;border-radius:2px;padding:4px 8px 4px 8px;font-size:6.4px;line-height:7.7px;color:#333}
.tweet:before{content:"";position:absolute;left:-9px;top:8px;border:5px solid transparent;border-right-color:#dcdcdc;border-top-color:#dcdcdc}
.tweet em{font-style:normal;color:var(--link)}
.tweet small{display:block;font-size:4.8px;color:#777;margin-top:3px}
.follow{position:absolute;left:120px;top:186px;font-size:4.8px;color:#444;display:flex;align-items:center;gap:3px}
.follow i{width:8px;height:8px;border-radius:50%;background:#2d74b8;display:inline-block}
.vline{position:absolute;left:175px;top:12px;width:1px;height:184px;background:var(--line)}
.post{position:absolute;left:190px;width:262px;height:48px}
.post .date{position:absolute;left:0;top:0;width:33px;height:33px;border-radius:50%;background:var(--green);border:2px solid #d9ecbf;color:#fff;text-align:center;font-family:"Ubuntu",sans-serif;font-weight:700;font-size:9px;line-height:8.5px;padding-top:7px}
.post b{position:absolute;left:42px;top:2px;font-size:7px;color:var(--ink);font-weight:400}
.post p{position:absolute;left:42px;top:14px;font-size:6.3px;white-space:nowrap}
.post a{position:absolute;left:42px;top:24px;font-size:4.8px;color:#333;text-decoration:underline}
.post .rule{position:absolute;left:0;top:41px;width:254px;border-top:1px dashed #bbb}
.footer{left:18px;top:790px;width:457px;height:31px;background:#efefef}
.footer p{position:absolute;left:15px;top:13px;font-size:5.4px;color:#555;font-weight:700}
.social{position:absolute;right:18px;top:9px;display:flex;gap:4px}
.social span{width:11px;height:11px;border:1px solid #999;border-radius:2px;background:#f7f7f7}
</style>
</head>
<body>
<div class="stage">
  <div class="page">
    <div class="abs logo">Maple &amp; Meadow</div>
    <nav class="abs nav">
      <a class="active" href="#">Home</a><a href="#">Our Services</a><a href="#">Whu Us?</a><a href="#">Exercises</a><a href="#">Relaxation</a><a href="#">Nutritions</a><a href="#">Contact Us</a>
    </nav>
    <div class="abs hero" role="img" aria-label="Spa still life with lit candles, cork-stoppered oil bottles and a white lily"></div>
    <div class="abs dots"><span></span><span></span><span></span><span></span></div>

    <section class="abs intro">
      <h1>Live long and prosper!</h1>
      <p>Lorem Ipsum is simply dummy text of the printing and typesetting industry. Lorem Ipsum has been the industry's standard dummy text ever since the 1500s, when an unknown printer</p>
      <span class="btn">Read More</span>
      <div class="divider"></div>
      <div class="thumb" style="left:212px"><div class="ph"><div role="img" aria-label="Person doing yoga on a beach" style="background:linear-gradient(#9fc3df,#d9d2c0 60%,#c9b79a)"></div></div><span>EXERCISES</span></div>
      <div class="thumb" style="left:292px"><div class="ph"><div role="img" aria-label="Oranges and fresh fruit" style="background:linear-gradient(135deg,#f2a01e,#e0541a 60%,#8a2a12)"></div></div><span>NUTRITION</span></div>
      <div class="thumb" style="left:372px"><div class="ph"><div role="img" aria-label="Relaxing spa facial treatment with a daisy" style="background:linear-gradient(135deg,#c98a63,#eadbd0 50%,#8e6a52)"></div></div><span>RELAXATION</span></div>
    </section>

    <section class="abs mid">
      <h2 style="left:13px;top:17px">Daily Specials</h2>
      <div class="special" style="top:42px"><div class="ph" role="img" aria-label="Citrus fruit"></div><b>Good Life</b><p>Lorem Ipsum is not simply random text. It has roots in a piece of classical</p><a>read more</a></div>
      <div class="special" style="top:88px"><div class="ph" role="img" aria-label="Citrus fruit"></div><b>Yoga Specials</b><p>Lorem Ipsum is not simply random text. It has roots in a piece of classical</p><a>read more</a></div>
      <div class="special" style="top:134px;border-bottom:0"><div class="ph" role="img" aria-label="Citrus fruit"></div><b>Nutrition</b><p>Lorem Ipsum is not simply random text. It has roots in a piece of classical</p><a>read more</a></div>

      <h2 style="left:161px;top:17px">Hours &amp; Locations</h2>
      <dl class="hours">
        <dt>Address</dt><dd>Meadow Lane, South Zone, CA 6425<br>(555) 010-4657</dd>
        <dt>Hours</dt><dd>Mon-Fri: 10am-11pm<br>Sat-sun: 11am-9am</dd>
      </dl>
      <div class="map" role="img" aria-label="Street map showing the location"></div>

      <h2 style="left:306px;top:17px">About Us</h2>
      <div class="about">
        <p style="top:43px">Lorem Ipsum is simply dummy text of the printing and typesetting industry. Lorem Ipsum has been the industry's standard dummy text ever since the 1500s, when an unknown printer took a galley of type and scrambled it to make a type specimen book lorem ipsum</p>
        <p style="top:102px">Lorem Ipsum is simply dummy text of the printing and typesetting industry. Lorem Ipsum has been the industry's standard dummy text ever since the 1500s, when an unknown</p>
        <span class="btn">Read More</span>
      </div>
    </section>

    <section class="abs lower">
      <h2 style="left:13px;top:16px">Tweets about Company</h2>
      <div class="tweet" style="top:44px">Lorem <em>ipsum dolor sit</em> lorem ipsum door lorem ipsum dolor sit demoscteare lorem ipsum lorem ipsum dolor ipsum dolor<small>about 15 seconds ago</small></div>
      <div class="tweet" style="top:100px">Lorem <em>ipsum dolor sit</em> lorem ipsum door lorem ipsum dolor sit<small>about 15 seconds ago</small></div>
      <div class="tweet" style="top:140px">Lorem <em>ipsum dolor sit</em> lorem ipsum door lorem ipsum dolor sit lorem ipsum dolor sit lorem<small>about 15 seconds ago</small></div>
      <div class="follow"><i></i>Follow Us →</div>
      <div class="vline"></div>

      <h2 style="left:190px;top:17px">Press and Events</h2>
      <div class="post" style="top:45px"><div class="date">21<br>Oct</div><b>An Example Blog Post</b><p>Lorem ipsum dolor sit amet, consectetur adipsicing elit, sed do elusmod</p><a>Read More →</a><div class="rule"></div></div>
      <div class="post" style="top:97px"><div class="date">18<br>Sep</div><b>An Example Blog Post</b><p>Lorem ipsum dolor sit amet, consectetur adipsicing elit, sed do elusmod</p><a>Read More →</a><div class="rule"></div></div>
      <div class="post" style="top:148px"><div class="date">07<br>Nov</div><b>An Example Blog Post</b><p>Lorem ipsum dolor sit amet, consectetur adipsicing elit, sed do elusmod</p><a>Read More →</a></div>
    </section>

    <footer class="abs footer">
      <p>Copyright 2011. All Rights Reserved.</p>
      <div class="social"><span></span><span></span><span></span></div>
    </footer>
  </div>
</div>
</body>
</html>
```